Heater product information sheets

I need the two product information sheets organized and laid out in a clean, easy to read attractive manner. These sheets are to advertise propane heaters for outdoor use and for wholesale to propane distributors, restaurants and homeowners that need to have propane heat as the winter ends and spring begins. They will be used for chilly evenings when people want to be outside eating, drinking and being social.
Updates

Low design quality

Target Market(s)

Restaurants, hospitality industry, special events, party rental companies, home owners with backyards

Font styles to use
Sans Serif

Requirements
Must have
• My logo in the document instead of k. Dahlby and company
Nice to have
• I would like to see Fire illustrated coming up the heaters and on the round glass, show it up the middle of the glass tube propane heater.

```html
<!DOCTYPE html>
<html lang="en">
<head>
<meta charset="utf-8">
<title>Outdoor Propane Heater – Product Sheet</title>
<link href="https://fonts.googleapis.com/css2?family=Josefin+Sans:wght@200;300;600;700&family=Poppins:wght@400;500&display=swap" rel="stylesheet">
<style>
  :root {
    --page-bg: #e6e6e6;
    --sheet: #f6f6f6;
    --ink: #333336;
    --orange: #ef942b;
    --dark: #1e1e20;
    --band: #e9e9eb;
    --label-bg: #ebebed;
    --white: #ffffff;
  }
  * { margin: 0; padding: 0; box-sizing: border-box; }
  html, body { width: 1180px; height: 1200px; overflow: hidden; background: var(--page-bg); }
  .sheet {
    position: absolute; left: 145px; top: 20px;
    width: 890px; height: 1160px;
    background: var(--sheet);
    font-family: "Poppins", sans-serif;
    color: var(--ink);
  }
  .title-main {
    position: absolute; left: 57px; top: 68px;
    font-family: "Josefin Sans", sans-serif; font-weight: 200;
    font-size: 92px; line-height: 1; letter-spacing: 0;
    white-space: nowrap;
  }
  .title-sub {
    position: absolute; left: 59px; top: 163px;
    font-family: "Josefin Sans", sans-serif; font-weight: 700;
    font-size: 54px; line-height: 1; color: var(--orange);
    white-space: nowrap;
  }
  .product-photo {
    position: absolute; left: 588px; top: 61px; width: 240px; height: 655px;
    background: linear-gradient(180deg, #c9cbcd 0%, #8e9194 25%, #3a3b3e 55%, #151517 100%);
    border-radius: 6px;
  }
  .section-label {
    position: absolute; left: 61px;
    height: 35px; padding: 0 14px 0 15px;
    background: var(--label-bg); border-left: 4px solid var(--orange);
    font-family: "Josefin Sans", sans-serif; font-weight: 600;
    font-size: 20px; letter-spacing: 2px; line-height: 39px;
  }
  .feature-list {
    position: absolute; left: 61px; list-style: none;
    font-size: 14px; line-height: 22px;
  }
  .feature-list li { position: relative; padding-left: 25px; }
  .feature-list li svg { position: absolute; left: 0; top: 4px; width: 15px; height: 15px; }
  .specs { top: 306px; line-height: 23.6px; }
  .details { top: 481px; }
  .details li { line-height: 16px; margin-bottom: 6.2px; }
  .audience-band {
    position: absolute; left: 0; top: 750px; width: 890px; height: 73px;
    background: var(--band);
  }
  .audience {
    position: absolute; top: 0; height: 73px;
    display: flex; align-items: center; gap: 16px;
    font-size: 13.5px; font-weight: 500; line-height: 17.5px; text-transform: uppercase;
  }
  .audience svg { width: 42px; height: 40px; flex: none; }
  .contact-panel {
    position: absolute; left: 0; top: 823px; width: 538px; height: 309px;
    background: var(--dark); color: var(--white);
  }
  .offer-panel {
    position: absolute; left: 538px; top: 823px; width: 352px; height: 309px;
    background: var(--orange); color: var(--dark);
  }
  .cta {
    position: absolute; left: 58px; top: 28px;
    font-family: "Josefin Sans", sans-serif; font-weight: 300;
    font-size: 52px; line-height: 59px;
    white-space: nowrap;
  }
  .company-name {
    position: absolute; left: 59px; top: 157px; height: 30px; padding: 0 7px;
    background: var(--orange); color: var(--dark);
    font-family: "Josefin Sans", sans-serif; font-weight: 700;
    font-size: 26px; line-height: 34px; letter-spacing: 2px; text-transform: uppercase;
    white-space: nowrap;
  }
  .contact-lines {
    position: absolute; left: 59px; top: 202px;
    font-size: 18px; line-height: 26.5px;
    white-space: nowrap;
  }
  .offer {
    position: absolute; left: 40px; display: flex; gap: 17px;
    font-size: 19px; font-weight: 500; line-height: 23.5px; text-transform: uppercase;
  }
  .offer svg { width: 28px; height: 28px; flex: none; margin-top: 2px; }
  .sheet-foot {
    position: absolute; left: 0; top: 1132px; width: 890px; height: 28px; background: var(--sheet);
  }
</style>
</head>
<body>
<svg width="0" height="0" style="position:absolute">
  <defs>
    <symbol id="tick" viewBox="0 0 24 24">
      <path d="M20 12a8 8 0 1 1-4-6.9" fill="none" stroke="currentColor" stroke-width="2.6" stroke-linecap="round"/>
      <path d="M7.5 11.5l4 4L22 4.5" fill="none" stroke="currentColor" stroke-width="2.6" stroke-linecap="round" stroke-linejoin="round"/>
    </symbol>
    <symbol id="star" viewBox="0 0 24 23">
      <path d="M12 1.5l3.2 6.6 7.2 1-5.2 5 1.3 7.2L12 17.9l-6.5 3.4 1.3-7.2-5.2-5 7.2-1z" fill="currentColor" stroke="currentColor" stroke-width="1.5" stroke-linejoin="round"/>
    </symbol>
  </defs>
</svg>

<main class="sheet">
  <h1 class="title-main">OUTDOOR</h1>
  <h2 class="title-sub">PROPANE HEATER</h2>

  <div class="product-photo" role="img" aria-label="Photo of a black powder-coated patio heater with a silver reflector hood, tall pole and round tank base"></div>

  <div class="section-label" style="top:256px">SPECIFICATIONS</div>
  <ul class="feature-list specs">
    <li><svg style="color:var(--orange)"><use href="#tick"/></svg>Powerful 48,000 BTU</li>
    <li><svg style="color:var(--orange)"><use href="#tick"/></svg>Black Powder Coated Finish</li>
    <li><svg style="color:var(--orange)"><use href="#tick"/></svg>Uses 20 lbs. Propane Tank</li>
    <li><svg style="color:var(--orange)"><use href="#tick"/></svg>CE, GS, AGA, CSA, with ETL certificate and ROHS approved</li>
  </ul>

  <div class="section-label" style="top:431px">ADDITIONAL DETAILS</div>
  <ul class="feature-list details">
    <li><svg style="color:var(--orange)"><use href="#tick"/></svg>Commercial Quality</li>
    <li><svg style="color:var(--orange)"><use href="#tick"/></svg>For Outdoor Use Only</li>
    <li><svg style="color:var(--orange)"><use href="#tick"/></svg>Conforms to ANSI STD Z83.26-2014 Certified to CSA</li>
    <li><svg style="color:var(--orange)"><use href="#tick"/></svg>STD 2.37-2014 Gas- fired outdoor infrared patio heaters<br>Safety Auto Shut Off Switch</li>
    <li><svg style="color:var(--orange)"><use href="#tick"/></svg>Thermostatic Control</li>
    <li><svg style="color:var(--orange)"><use href="#tick"/></svg>Base Diameter 17" - Anti-Tip Design</li>
    <li><svg style="color:var(--orange)"><use href="#tick"/></svg>Standard Wheels - Tilt &amp; Move</li>
    <li><svg style="color:var(--orange)"><use href="#tick"/></svg>Run time: 8-10 hours with standard 20 lbs. Propane tank</li>
    <li><svg style="color:var(--orange)"><use href="#tick"/></svg>88" Tall</li>
    <li><svg style="color:var(--orange)"><use href="#tick"/></svg>Heating Area: 200 sq. ft</li>
  </ul>

  <section class="audience-band">
    <div class="audience" style="left:58px"><svg style="color:var(--orange)"><use href="#star"/></svg><span>Rentals for<br>live events</span></div>
    <div class="audience" style="left:371px"><svg style="color:var(--orange)"><use href="#star"/></svg><span>Rentals for<br>restaurants &amp;<br>catering halls</span></div>
    <div class="audience" style="left:647px"><svg style="color:var(--orange)"><use href="#star"/></svg><span>Purchase for<br>your home or<br>business</span></div>
  </section>

  <section class="contact-panel">
    <p class="cta">TO RENT<br>OR PURCHASE</p>
    <p class="company-name">K. Dahlby &amp; Company</p>
    <p class="contact-lines">555-014-2290<br>Nora@KDpartyrental.com<br>42 Orchard Lane Millbrook, NJ 07042</p>
  </section>

  <section class="offer-panel">
    <div class="offer" style="top:44px"><svg style="color:var(--dark)"><use href="#tick"/></svg><span>Starting at<br>$250 each</span></div>
    <div class="offer" style="top:121px"><svg style="color:var(--dark)"><use href="#tick"/></svg><span>Discounts for<br>large quantity<br>orders</span></div>
    <div class="offer" style="top:222px"><svg style="color:var(--dark)"><use href="#tick"/></svg><span>Assembly &amp;<br>delivery available<br>upon request</span></div>
  </section>

  <div class="sheet-foot"></div>
</main>
</body>
</html>
```